DMR Property - Business Cards

Looking for a business card & general letterhead, signage etc design for our new logo.

Colours:
000a20
0056a2
00b5ef
0088ce
68cef2

Fonts:
Poppins
Karla

Please keep look and feel of new brand - example in the zip package I sent.

```html
<!DOCTYPE html>
<html lang="en">
<head>
<meta charset="utf-8">
<title>DMR Property – Business Cards</title>
<link rel="stylesheet" href="https://fonts.googleapis.com/css2?family=Poppins:wght@400;500;600;800&display=swap">
<style>
  :root {
    --ink: #000a20;
    --brand-blue: #0056a2;
    --bright-blue: #00b5ef;
    --mid-blue: #0088ce;
    --sky-blue: #68cef2;
    --paper: #ffffff;
    --stage: #1b1d22;
    --text-dark: #1a1a1a;
  }
  * { box-sizing: border-box; margin: 0; padding: 0; }
  html, body { width: 1200px; height: 900px; overflow: hidden; }
  body {
    background: var(--stage);
    font-family: "Poppins", sans-serif;
    position: relative;
  }
  .card {
    position: absolute;
    left: 250px;
    width: 700px;
    height: 400px;
    overflow: hidden;
  }
  .card--front { top: 35px; background: var(--paper); }
  .card--back { top: 465px; background: var(--brand-blue); }

  .front-wave { position: absolute; inset: 0; }

  .wordmark {
    position: absolute;
    font-family: "Poppins", sans-serif;
    font-weight: 800;
    letter-spacing: 1px;
    line-height: 1;
    white-space: nowrap;
  }
  .card--front .wordmark {
    left: 50px; top: 140px;
    font-size: 40px;
    color: var(--brand-blue);
  }
  .card--back .wordmark {
    right: 60px; bottom: 60px;
    font-size: 34px;
    color: var(--paper);
  }

  .divider {
    position: absolute;
    left: 372px; top: 70px;
    width: 1px; height: 230px;
    background: var(--mid-blue);
  }

  .contact {
    position: absolute;
    left: 396px; top: 78px;
    color: var(--text-dark);
  }
  .contact__name {
    font-weight: 800;
    font-size: 28px;
    line-height: 1.1;
    color: var(--brand-blue);
    letter-spacing: 0.5px;
  }
  .contact__name span { color: var(--mid-blue); }
  .contact__role {
    font-size: 15px;
    margin-bottom: 18px;
  }
  .contact__list { list-style: none; font-size: 15px; line-height: 1.55; }
  .contact__list li { display: flex; align-items: center; gap: 8px; }
  .contact__list svg { width: 13px; height: 13px; flex: none; }
  .contact__address { font-size: 15px; line-height: 1.5; margin-top: 10px; }

  .back-pattern {
    position: absolute; inset: 0;
    background: linear-gradient(135deg, #0a63c4 0%, var(--brand-blue) 55%, #0a4d9a 100%);
  }
</style>
</head>
<body>

  <section class="card card--front" aria-label="Business card front">
    <svg class="front-wave" viewBox="0 0 700 400" preserveAspectRatio="none" aria-hidden="true">
      <path d="M0 255 C 140 240, 230 270, 330 320 C 430 370, 540 395, 700 398 L700 400 L0 400 Z" fill="var(--brand-blue)"/>
      <path d="M0 252 C 150 236, 240 262, 340 312 C 440 362, 550 388, 700 392" fill="none" stroke="var(--bright-blue)" stroke-width="4"/>
    </svg>

    <div class="wordmark">DMR Property</div>
    <div class="divider"></div>

    <div class="contact">
      <h1 class="contact__name">DANA <span>REYES</span></h1>
      <p class="contact__role">Founder &amp; Principal</p>
      <ul class="contact__list">
        <li>
          <svg viewBox="0 0 16 16"><path d="M4 1 L6.5 4 L5 6 C6 8 8 10 10 11 L12 9.5 L15 12 L13 15 C7 15 1 9 1 3 Z" fill="var(--brand-blue)"/></svg>
          +1- 555-014-2290
        </li>
        <li>
          <svg viewBox="0 0 16 16"><rect x="1" y="3" width="14" height="10" fill="none" stroke="var(--brand-blue)" stroke-width="1.6"/><path d="M1 3 L8 9 L15 3" fill="none" stroke="var(--brand-blue)" stroke-width="1.6"/></svg>
          info@dmrproperty.com
        </li>
        <li>
          <svg viewBox="0 0 16 16"><circle cx="8" cy="8" r="6.5" fill="none" stroke="var(--brand-blue)" stroke-width="1.5"/><ellipse cx="8" cy="8" rx="3" ry="6.5" fill="none" stroke="var(--brand-blue)" stroke-width="1.2"/><path d="M1.5 8 H14.5" stroke="var(--brand-blue)" stroke-width="1.2"/></svg>
          www.dmrproperty.com
        </li>
      </ul>
      <p class="contact__address">4120 Harbor View Road<br>#18, Suite Lakeside Park</p>
    </div>
  </section>

  <section class="card card--back" aria-label="Business card back">
    <div class="back-pattern" role="img" aria-label="Repeating brand mark pattern in blue tones"></div>
    <div class="wordmark">DMR Property</div>
  </section>

</body>
</html>
```